Business Card for a Wellness and Aesthetic Center

I'd like to have a business card design for a Wellness and Aesthetic Center based in the Philippines called "Silvermoss Wellness and Aesthetic Inc." They provide services such as medical and aesthetic dermatology. Specializing on cosmetic and anti-aging procedures.

The target market of the business is mostly women from the upper class from 30 to 60 years old.

The feel and look of the card should be feminine, modern, minimalist and classy.

The colors to play with are gold and black.

The front part should contain:
- Name (example: Marisol Teravid Pangilan, MD)
- Designation (example: Medical Director)
- Company Logo

The back part should contain:
- Company Logo
- Address
- Contact Details
- Website

For more details and inspiration you may visit their website at http://silvermossph.com/

Thank you very much!

Target Market(s)

Women from the upper class from 30 to 60 years old.

Industry/Entity Type

Business

Contact Information for Business Card

- Company Logo

- Company Logo
- Address
- Contact Details
- Website

Font styles to use
Serif
Script

Colors
ffc214
fece3e
faa54b
f78f20
000000

Requirements
Must have
• Design should be feminine, modern, minimalist/simple and classy.
Nice to have
• You can play with lines, curves, gardient and be creative on the placement of texts and logo.
Should not have
• Pictures like body, face or nature scene.

```html
<!DOCTYPE html>
<html lang="en">
<head>
<meta charset="utf-8">
<title>Silvermoss Business Card</title>
<link rel="stylesheet" href="https://fonts.googleapis.com/css2?family=Arimo:wght@400;700&display=swap">
<style>
  :root {
    --bg: #3a3331;
    --card-black: #1f1b19;
    --gold: #f0a52a;
    --ink: #2a1a08;
  }
  * { margin: 0; padding: 0; box-sizing: border-box; }
  html, body { width: 1200px; height: 768px; overflow: hidden; background: var(--bg); }
  .canvas {
    position: relative; width: 1200px; height: 768px;
    display: flex; align-items: center; justify-content: center; gap: 60px;
    font-family: "Arimo", Arial, sans-serif;
  }
  .card {
    position: relative; width: 500px; height: 286px;
    background: var(--card-black); border-radius: 12px; overflow: hidden;
    box-shadow: 0 10px 30px rgba(0,0,0,.45);
  }
  .brand {
    position: absolute; left: 0; right: 0; top: 84px;
    display: flex; align-items: center; justify-content: center; gap: 12px;
    color: var(--gold); font-weight: 400; font-size: 40px; letter-spacing: 1px;
  }
  .brand-dot { width: 14px; height: 14px; border-radius: 50%; background: var(--gold); }
  .holder {
    position: absolute; right: 34px; bottom: 36px; text-align: center; color: var(--gold);
  }
  .holder-name { font-size: 16px; }
  .holder-role { font-size: 10px; margin-top: 4px; }
  .card-back .brand { top: 44px; }
  .wave { position: absolute; left: 0; top: 0; width: 500px; height: 286px; }
  .contact {
    position: absolute; right: 24px; bottom: 16px; width: 226px;
    color: var(--ink); font-size: 11px; line-height: 1.3; list-style: none;
  }
  .contact li { display: flex; align-items: flex-start; gap: 8px; margin-top: 3px; }
  .contact svg { width: 11px; height: 11px; flex: none; margin-top: 2px; fill: var(--ink); }
</style>
</head>
<body>
<main class="canvas">
  <section class="card card-front">
    <div class="brand"><span class="brand-dot"></span>Silvermoss</div>
    <div class="holder">
      <p class="holder-name">Marisol Teravid Pangilan</p>
      <p class="holder-role">Medical Director</p>
    </div>
  </section>

  <section class="card card-back">
    <svg class="wave" viewBox="0 0 500 286" aria-hidden="true">
      <defs>
        <linearGradient id="goldFill" x1="0" y1="0" x2="1" y2="0">
          <stop offset="0" stop-color="#9a6a22"/>
          <stop offset="0.45" stop-color="#c8953a"/>
          <stop offset="0.8" stop-color="#b07c2c"/>
          <stop offset="1" stop-color="#6e4618"/>
        </linearGradient>
        <linearGradient id="goldEdge" x1="0" y1="0" x2="1" y2="0">
          <stop offset="0" stop-color="#c99a4a"/>
          <stop offset="0.35" stop-color="#fff3cf"/>
          <stop offset="0.6" stop-color="#e0b45a"/>
          <stop offset="0.8" stop-color="#fbe6a8"/>
          <stop offset="1" stop-color="#b98a38"/>
        </linearGradient>
      </defs>
      <path d="M0 116 C 150 110, 260 124, 340 138 S 460 152, 500 146 L500 286 L0 286 Z" fill="url(#goldEdge)"/>
      <path d="M0 126 C 150 120, 260 134, 340 148 S 460 162, 500 156 L500 286 L0 286 Z" fill="url(#goldFill)"/>
    </svg>
    <div class="brand"><span class="brand-dot"></span>Silvermoss</div>
    <ul class="contact">
      <li><svg viewBox="0 0 12 12"><path d="M2.5 1 L4.5 1 L5.3 3.5 L4 4.6 C4.7 6 6 7.3 7.4 8 L8.5 6.7 L11 7.5 L11 9.5 C11 10.3 10.3 11 9.5 11 C5 11 1 7 1 2.5 C1 1.7 1.7 1 2.5 1Z"/></svg>(632) 418-3096</li>
      <li><svg viewBox="0 0 12 12"><path d="M1 2.5 H11 V9.5 H1 Z M1.6 3 L6 6.5 L10.4 3" stroke="#c8953a" stroke-width=".7"/></svg>beauty@silvermossph.com</li>
      <li><svg viewBox="0 0 12 12"><circle cx="6" cy="6" r="5" fill="none" stroke="#2a1a08" stroke-width="1"/><path d="M1 6 H11 M6 1 C3.5 4 3.5 8 6 11 M6 1 C8.5 4 8.5 8 6 11" fill="none" stroke="#2a1a08" stroke-width=".8"/></svg>www.silvermossph.com</li>
      <li><svg viewBox="0 0 12 12"><path d="M6 0.5 C3.8 0.5 2.2 2.1 2.2 4.2 C2.2 7 6 11.5 6 11.5 C6 11.5 9.8 7 9.8 4.2 C9.8 2.1 8.2 0.5 6 0.5Z M6 2.8 A1.4 1.4 0 1 0 6 5.6 A1.4 1.4 0 1 0 6 2.8Z"/></svg><span>Basement, Halden Tower<br>Serrano Business Park<br>Lakeview, Marisco City, PH</span></li>
    </ul>
  </section>
</main>
</body>
</html>
```